DL size flyer for Autism Consultancy website

We need a printed flyer DL size ( 210mmx99mm) for our Autism Consultancy website www.brightpathkids.nz which provides therapy for autistic children.
I want the flyer to look consistent with the website’s design. Please feel free to use the colour scheme, fonts, icons or any images from www.brightpathkids.nz.It should be easy to see “Autism” or “Autistic” word from a distance.
Please use either an oversized logo or make “Do you have a verbal and able autistic child?” more prominent.
Please do not convert the text fields to outlines, i.e. I need to be able to edit any text after.The final design should be either in Adobe Illustrator or Adobe Photoshop format.
The Specs for the flyer are
Document Trim Size99 x 210 mm 1169 x 2480 pixels
Full Bleed Size102 x 213 mm 1205 x 2516 pixels
Our Logo https://1drv.ms/u/s!AoH0rRjDY2GYg6QtU-xjoVlmslKp6gPlease
use this photo for the front side https://qzdropbin.io/f/Pw4KcN8rTyH2mXs6BvLd9QeFz1Gj
another one for reverse
https://qzdropbin.io/f/Rk2HsV5nWqJ7tZc3MfXb8LpYd4Ne
Please use the following content:
Do you have a verbal and able autistic child?
We use child-centred, modern and innovative approaches
Teaching autistic children to bond, laugh and play.
We work with schools
We help autistic children to develop social minds
We offer:
• Specialist assessments
• Consultations for parents & schools
• Social learning programmes
• Social-cognitive therapy
We can create an individual learning path, best suited for your child.
Our programmes and interventions include:
• Chatter Quest
• Peer Bright
• Team Puzzles
• Tingle Words
• Pebble Tales
• Pembrook Speech Ladder
• Vorlin Method
• BRIMLE Method
• Tandem Pattern Coaching
contact details on both sides:
www.brightpathkids.nz
info@brightpathkids.nz
(09) 57-318-46

```html
<!DOCTYPE html>
<html lang="en">
<head>
<meta charset="utf-8">
<title>Bright Path Kids – DL Flyer</title>
<link rel="stylesheet" href="https://fonts.googleapis.com/css2?family=Montserrat:wght@500;600;700&family=Play:wght@700&display=swap">
<style>
  :root {
    --teal: #56c4bf;
    --teal-light: #84d6d2;
    --teal-pale: #a9e3e0;
    --navy: #1f2a5a;
    --yellow: #fcd626;
    --grey-text: #9b9b9b;
    --grey-panel: #ececec;
    --white: #ffffff;
    --page: #e8e5e1;
  }
  * { box-sizing: border-box; margin: 0; padding: 0; }
  html, body { width: 1200px; height: 1120px; overflow: hidden; }
  body { background: var(--page); font-family: "Montserrat", Arial, sans-serif; position: relative; }

  .flyer { position: absolute; width: 490px; height: 1037px; background: var(--teal); overflow: hidden; box-shadow: 0 3px 10px rgba(0,0,0,.18); }
  .flyer--front { left: 112px; top: 24px; }
  .flyer--back { left: 614px; top: 47px; }

  .abs { position: absolute; left: 0; width: 100%; }
  .display { font-family: "Play", "Trebuchet MS", sans-serif; font-weight: 700; color: var(--navy); text-align: center; letter-spacing: .5px; }

  /* Front */
  .brand-bar { top: 0; height: 118px; background: var(--white); display: flex; align-items: center; justify-content: center; gap: 12px; }
  .brand-dot { width: 34px; height: 34px; border-radius: 50%; background: var(--yellow); }
  .brand-name { font-family: "Montserrat", Arial, sans-serif; font-weight: 700; font-size: 26px; color: var(--navy); }
  .photo { background: linear-gradient(120deg, #c98a5a 0%, #e9dccd 35%, #f4efe8 60%, #d9b08c 100%); }
  .photo--front { top: 118px; height: 380px; }
  .wave { position: absolute; left: 0; width: 100%; }
  .front-wave { top: 430px; height: 80px; }
  .headline { top: 548px; font-size: 31px; line-height: 40px; font-weight: 600; color: var(--white); text-align: center; white-space: nowrap; letter-spacing: -0.2px; }
  .claims { top: 652px; }
  .claim { font-size: 23px; line-height: 31px; margin-bottom: 20px; }

  .contact { top: 964px; height: 73px; background: var(--yellow); display: flex; flex-direction: column; align-items: center; justify-content: center; gap: 4px; color: var(--navy); font-weight: 600; font-size: 19px; }
  .contact-row { display: flex; gap: 18px; align-items: center; }
  .contact-item { display: flex; align-items: center; gap: 7px; }
  .contact-item svg { width: 18px; height: 18px; fill: var(--navy); }

  /* Back */
  .tagline { top: 28px; font-size: 23px; line-height: 31px; }
  .back-wave { top: 120px; height: 70px; }
  .photo--back { top: 178px; height: 352px; background: linear-gradient(135deg, #d9b592 0%, #ecd3b4 45%, #e0b68c 100%); }
  .offer { top: 530px; height: 162px; background: var(--white); padding-top: 22px; }
  .panel-title { font-weight: 600; font-size: 26px; line-height: 30px; color: var(--navy); text-align: center; }
  .bullets { display: grid; grid-template-columns: 205px 1fr; column-gap: 8px; padding: 0 18px 0 22px; margin-top: 14px; }
  .bullets ul { list-style: none; }
  .bullets li { position: relative; padding-left: 12px; font-size: 14.5px; line-height: 18px; font-weight: 500; color: var(--grey-text); margin-bottom: 9px; white-space: normal; }
  .bullets li::before { content: ""; position: absolute; left: 0; top: 7px; width: 5px; height: 5px; border-radius: 50%; background: var(--grey-text); }
  .programmes { top: 692px; height: 272px; background: var(--grey-panel); padding-top: 22px; }
  .programmes .bullets { margin-top: 24px; }
  .programmes .bullets li { margin-bottom: 10px; }
</style>
</head>
<body>

<section class="flyer flyer--front">
  <header class="abs brand-bar">
    <span class="brand-dot"></span>
    <span class="brand-name">Bright Path Kids</span>
  </header>
  <div class="abs photo photo--front" role="img" aria-label="Photo of a smiling boy holding a teddy bear while sitting with a therapist in a bright playroom"></div>
  <svg class="wave front-wave" viewBox="0 0 490 80" preserveAspectRatio="none" aria-hidden="true">
    <path d="M0 20 C80 0 160 30 250 15 C340 0 420 25 490 12 L490 80 L0 80 Z" fill="var(--teal-pale)"/>
    <path d="M0 40 C90 25 170 50 260 36 C350 22 420 45 490 34 L490 80 L0 80 Z" fill="var(--teal-light)"/>
    <path d="M0 60 C100 48 190 70 280 58 C370 46 430 62 490 55 L490 80 L0 80 Z" fill="var(--teal)"/>
  </svg>
  <h1 class="abs headline">Do you have a verbal<br>and able autistic child?</h1>
  <div class="abs claims">
    <p class="display claim">We use child-centred, modern<br>and innovative approaches</p>
    <p class="display claim">Teaching autistic children to<br>bond, laugh and play.</p>
    <p class="display claim">We work with schools</p>
    <p class="display claim">We help autistic children to<br>develop social minds</p>
  </div>
  <footer class="abs contact">
    <div>www.brightpathkids.nz</div>
    <div class="contact-row">
      <span class="contact-item"><svg viewBox="0 0 24 24"><path d="M2 5h20v14H2z" fill="var(--navy)"/><path d="M3 6l9 7 9-7" stroke="var(--yellow)" stroke-width="2" fill="none"/></svg>info@brightpathkids.nz</span>
      <span class="contact-item"><svg viewBox="0 0 24 24"><path d="M6.6 10.8a15 15 0 0 0 6.6 6.6l2.2-2.2a1 1 0 0 1 1-.25 11.4 11.4 0 0 0 3.6.57 1 1 0 0 1 1 1V20a1 1 0 0 1-1 1A17 17 0 0 1 3 4a1 1 0 0 1 1-1h3.5a1 1 0 0 1 1 1c0 1.25.2 2.45.57 3.57a1 1 0 0 1-.25 1z"/></svg>(09) 57-318-46</span>
    </div>
  </footer>
</section>

<section class="flyer flyer--back">
  <p class="abs display tagline">We can create an individual learning<br>path, best suited for your child.</p>
  <svg class="wave back-wave" viewBox="0 0 490 70" preserveAspectRatio="none" aria-hidden="true">
    <path d="M0 10 C90 25 170 0 260 14 C350 28 420 5 490 16 L490 70 L0 70 Z" fill="var(--teal-light)"/>
    <path d="M0 35 C100 50 180 25 270 40 C360 55 430 30 490 42 L490 70 L0 70 Z" fill="var(--teal-pale)"/>
  </svg>
  <div class="abs photo photo--back" role="img" aria-label="Photo of a boy in a striped shirt playing with toy cars spread on a wooden floor"></div>
  <div class="abs offer">
    <h2 class="panel-title">We offer:</h2>
    <div class="bullets">
      <ul>
        <li>Specialist assessments</li>
        <li>Consultations for<br>parents &amp; schools</li>
      </ul>
      <ul>
        <li>Social learning programmes</li>
        <li>Social-cognitive therapy</li>
      </ul>
    </div>
  </div>
  <div class="abs programmes">
    <h2 class="panel-title">Our programmes and<br>interventions include:</h2>
    <div class="bullets">
      <ul>
        <li>Chatter Quest</li>
        <li>Peer Bright</li>
        <li>Team Puzzles</li>
        <li>Tingle Words</li>
        <li>Pebble Tales</li>
      </ul>
      <ul>
        <li>Pembrook Speech Ladder</li>
        <li>Vorlin Method</li>
        <li>BRIMLE Method</li>
        <li>Tandem Pattern Coaching</li>
      </ul>
    </div>
  </div>
  <footer class="abs contact">
    <div>www.brightpathkids.nz</div>
    <div class="contact-row">
      <span class="contact-item"><svg viewBox="0 0 24 24"><path d="M2 5h20v14H2z" fill="var(--navy)"/><path d="M3 6l9 7 9-7" stroke="var(--yellow)" stroke-width="2" fill="none"/></svg>info@brightpathkids.nz</span>
      <span class="contact-item"><svg viewBox="0 0 24 24"><path d="M6.6 10.8a15 15 0 0 0 6.6 6.6l2.2-2.2a1 1 0 0 1 1-.25 11.4 11.4 0 0 0 3.6.57 1 1 0 0 1 1 1V20a1 1 0 0 1-1 1A17 17 0 0 1 3 4a1 1 0 0 1 1-1h3.5a1 1 0 0 1 1 1c0 1.25.2 2.45.57 3.57a1 1 0 0 1-.25 1z"/></svg>(09) 57-318-46</span>
    </div>
  </footer>
</section>

</body>
</html>
```